PRVD Traditional Business Card Project

Please see attached....just a simple business card... on attachment- please use the exact font, style, etc as the attached "Pat Everard Wynne" card... however, replace with the "Owen Reginald Talbot" text and address below the card.

```html
<!DOCTYPE html>
<html lang="en">
<head>
<meta charset="utf-8">
<title>PRVD Business Card</title>
<link rel="stylesheet" href="https://fonts.googleapis.com/css2?family=Tinos:wght@700&family=Michroma&family=Montserrat:wght@500&display=swap">
<style>
  :root {
    --backdrop: #e4e4e4;
    --card-navy: #050f33;
    --gold: #d8b94a;
    --card-shadow: rgba(0, 0, 0, 0.45);
  }
  * { margin: 0; padding: 0; box-sizing: border-box; }
  html, body {
    width: 1200px;
    height: 900px;
    overflow: hidden;
    background: var(--backdrop);
  }
  .canvas {
    position: relative;
    width: 1200px;
    height: 900px;
  }
  .card {
    position: absolute;
    left: 302px;
    width: 560px;
    height: 344px;
    background: var(--card-navy);
    color: var(--gold);
    box-shadow: 3px 4px 6px var(--card-shadow);
  }
  .card--front { top: 82px; }
  .card--back { top: 448px; height: 343px; }

  .firm-name {
    font-family: "Tinos", "Times New Roman", serif;
    font-weight: 700;
    font-variant: small-caps;
    white-space: nowrap;
  }
  .firm-type {
    font-family: "Michroma", "Arial", sans-serif;
    text-transform: uppercase;
    white-space: nowrap;
  }

  .front-firm {
    position: absolute;
    left: 30px;
    top: 30px;
  }
  .front-firm .firm-name { font-size: 21px; letter-spacing: 0.3px; }
  .front-firm .firm-type {
    font-size: 10px;
    letter-spacing: 3px;
    margin-top: 2px;
    padding-left: 12px;
  }

  .person {
    position: absolute;
    left: 0;
    right: 0;
    top: 132px;
    text-align: center;
  }
  .person-name {
    font-family: "Tinos", "Times New Roman", serif;
    font-weight: 700;
    font-variant: small-caps;
    font-size: 28px;
    letter-spacing: 0.5px;
  }
  .person-title {
    font-family: "Michroma", "Arial", sans-serif;
    font-size: 13px;
    letter-spacing: 4px;
    margin-top: 2px;
  }

  .contact {
    position: absolute;
    top: 253px;
    font-family: "Montserrat", "Helvetica", sans-serif;
    font-weight: 500;
    font-size: 14px;
    line-height: 19px;
  }
  .contact--address { left: 29px; font-size: 13.5px; }
  .contact--lines { right: 28px; text-align: right; font-size: 15px; line-height: 20px; }
  .contact-item { display: block; }

  .back-firm {
    position: absolute;
    left: 0;
    right: 0;
    top: 136px;
    text-align: center;
  }
  .back-firm .firm-name { font-size: 30px; letter-spacing: 0.4px; }
  .back-firm .firm-type {
    font-size: 15px;
    letter-spacing: 5px;
    margin-top: 8px;
  }
</style>
</head>
<body>
<main class="canvas">
  <section class="card card--front" aria-label="Business card front">
    <header class="front-firm">
      <div class="firm-name">Pacific Ridge</div>
      <div class="firm-type">Valley Defenders, PLC</div>
    </header>

    <div class="person">
      <div class="person-name">Owen Reginald Talbot</div>
      <div class="person-title">ATTORNEY AT LAW</div>
    </div>

    <address class="contact contact--address" style="font-style: normal;">
      <span class="contact-item">2740 CEDAR LANE, SUITE B</span>
      <span class="contact-item">MAPLE GROVE, CA 92814</span>
      <span class="contact-item">www.lawprvd.com</span>
    </address>

    <div class="contact contact--lines">
      <span class="contact-item">TEL:(555) 214-3300</span>
      <span class="contact-item">FAX:(555) 214-3301</span>
      <span class="contact-item">otalbot@lawprvd.com</span>
    </div>
  </section>

  <section class="card card--back" aria-label="Business card back">
    <div class="back-firm">
      <div class="firm-name">Pacific Ridge</div>
      <div class="firm-type">Valley Defenders, PLC</div>
    </div>
  </section>
</main>
</body>
</html>
```